a promotional poster design to promote our upcoming event. We want the date to be promoted as "Save the Date" for Sunday 4th July 2021.

Requirements
Must have
• the following text;

Save the Date! (stand out)
Sunday 4th July 2021 (stand out)
KTRB Family Mixed Netball Carnival
Nice to have
• make the date stand out. We want people to lock in the date we're promoting.

```html
<!DOCTYPE html>
<html lang="en">
<head>
<meta charset="utf-8">
<title>KTRB Family Mixed Netball Carnival – Save the Date</title>
<link rel="stylesheet" href="https://fonts.googleapis.com/css2?family=Arimo:wght@400;700&display=swap">
<style>
  :root {
    --poster-red: #ed1c24;
    --poster-white: #ffffff;
    --ball-tint: #f7a9ac;
    --brand-ink: #111111;
  }
  html, body {
    margin: 0;
    padding: 0;
    width: 848px;
    height: 1200px;
    overflow: hidden;
    background: var(--poster-red);
  }
  .poster {
    display: block;
    width: 848px;
    height: 1200px;
    font-family: "Arimo", Arial, sans-serif;
  }
  .poster__bg { fill: var(--poster-red); }
  .event-title { fill: var(--poster-white); font-size: 60px; }
  .headline { fill: var(--poster-white); font-size: 170px; }
  .divider { fill: var(--poster-white); }
  .date { fill: var(--poster-white); }
  .date--day { font-size: 88px; }
  .date--num { font-size: 80px; }
  .date--month { font-size: 80px; }
  .date--year { font-size: 80px; }
  .brand-name { fill: var(--brand-ink); font-size: 16px; font-weight: 700; }
</style>
</head>
<body>
<svg class="poster" viewBox="0 0 848 1200" xmlns="http://www.w3.org/2000/svg">
  <defs>
    <radialGradient id="ballGlow" cx="0.5" cy="0.5" r="0.5">
      <stop offset="0" stop-color="#f7a9ac" stop-opacity="0.55"/>
      <stop offset="0.85" stop-color="#f7a9ac" stop-opacity="0.35"/>
      <stop offset="1" stop-color="#f7a9ac" stop-opacity="0"/>
    </radialGradient>
    <linearGradient id="waveGlow" x1="0" y1="0" x2="1" y2="1">
      <stop offset="0" stop-color="#ffffff" stop-opacity="0.18"/>
      <stop offset="1" stop-color="#ffffff" stop-opacity="0.04"/>
    </linearGradient>
  </defs>

  <rect class="poster__bg" x="0" y="0" width="848" height="1200"/>

  <!-- Decorative areas -->
  <rect x="0" y="968" width="480" height="232" fill="url(#waveGlow)" role="img" aria-label="Sweeping white speed-line waves across the lower left"/>
  <circle cx="700" cy="1045" r="300" fill="url(#ballGlow)" role="img" aria-label="Dotted halftone netball graphic in the lower right corner"/>

  <!-- Header -->
  <g class="event-header">
    <text class="event-title" x="174" y="145" textLength="523" lengthAdjust="spacingAndGlyphs">KTRB Family Mixed</text>
    <text class="event-title" x="218" y="199" textLength="400" lengthAdjust="spacingAndGlyphs">Netball Carnival</text>
    <rect class="divider" x="83" y="242" width="683" height="8"/>
  </g>

  <!-- Save the date -->
  <g class="headline-block">
    <text class="headline" x="83" y="477" textLength="359" lengthAdjust="spacingAndGlyphs">SAVE</text>
    <text class="headline" x="174" y="619" textLength="268" lengthAdjust="spacingAndGlyphs">THE</text>
    <text class="headline" x="87" y="763" textLength="355" lengthAdjust="spacingAndGlyphs">DATE</text>
    <rect class="divider" x="477" y="356" width="13" height="407"/>
  </g>

  <!-- Date -->
  <g class="date-block">
    <text class="date date--day" x="524" y="481" textLength="242" lengthAdjust="spacingAndGlyphs">Sunday</text>
    <text class="date date--num" x="592" y="580" textLength="122" lengthAdjust="spacingAndGlyphs">4th</text>
    <text class="date date--month" x="561" y="645" textLength="156" lengthAdjust="spacingAndGlyphs">July</text>
    <text class="date date--year" x="543" y="726" textLength="194" lengthAdjust="spacingAndGlyphs">2021</text>
  </g>

  <!-- Organiser name -->
  <g class="brand">
    <text class="brand-name" x="360" y="1073" textLength="165" lengthAdjust="spacingAndGlyphs">KESTREL RIDGE</text>
    <text class="brand-name" x="384" y="1095" textLength="118" lengthAdjust="spacingAndGlyphs">HEALTH BOARD</text>
  </g>
</svg>
</body>
</html>
```